Design a Mobile First Website for a Salad Resturant

** WEBSITE LIKE AN APP, NOT LANDING PAGE **

1. Homepage
Objective: Introduce the brand and direct visitors to either start creating their custom salad or explore the menu of pre-designed salads.
Design Elements:
Clean and minimalistic layout with high-quality images of fresh salads.
Two prominent buttons: "Create Your Salad" and "Our Salads".
Brief welcome message that highlights the freshness and quality of ingredients.

2. Create Your Salad Page
Objective: Allow customers to design their salad from a list of ingredients.
Design Elements:
Interactive, step-by-step builder interface where customers can select ingredients. Each ingredient category (like greens, proteins, toppings, dressings) should be a separate step in the process.
Visual representation of their salad being built as they select ingredients.
Information icons next to each ingredient for dietary information (e.g., vegan, gluten-free, calories).
Option to save favorite combinations or reorder past salads.
Clear price updates as they add or remove ingredients.

3. Our Salads Page
Objective: Showcase a list of pre-designed salad options that customers can quickly choose from.
Design Elements:
Grid layout with images and brief descriptions of each pre-designed salad.
Include customer reviews and ratings for each salad.
Easy "Add to Cart" option from this page.

4. Cart and Checkout Page
Objective: Streamline the checkout process with minimal steps.
Design Elements:
Summary of order with options to modify quantities or remove items.
Simple form for entering delivery details, with the ability to remember details for returning customers.
Secure payment gateway integration.
A confirmation screen with estimated delivery time and order tracking capabilities.

5. Mobile Optimization
Approach: Since this is a "Mobile First Design", ensure that:
The website is responsive and elements like buttons, text, and images scale properly across different devices.
Touch-friendly interfaces with large tap targets for ease of use on mobile devices.
Fast loading times by optimizing images and using mobile-first coding practices.

Target Market(s)

Food

Industry/Entity Type

Food

Number of Pages Required

4 page

Requirements
Must have
• Modren Design, Mobile First

```html
<!DOCTYPE html>
<html lang="en">
<head>
<meta charset="utf-8">
<title>Verdi Salad – Mobile Screens</title>
<link rel="stylesheet" href="https://fonts.googleapis.com/css2?family=Rubik:wght@400;500;700&display=swap">
<style>
:root{
  --stage:#b9b9b7;
  --screen:#ffffff;
  --cream:#f2ecdd;
  --cream-deep:#ebe2cc;
  --ink:#1c1c1c;
  --muted:#555;
  --slate:#4b5f75;
  --gold:#f0a800;
  --star:#f5b400;
  --red:#d9302c;
  --line:#eee4d6;
}
*{box-sizing:border-box;margin:0;padding:0}
html,body{width:1200px;height:974px;overflow:hidden}
body{background:var(--stage);font-family:"Rubik",sans-serif;color:var(--ink);position:relative}
.screen{position:absolute;width:233px;background:linear-gradient(180deg,var(--cream) 0%,#fbf8f1 40%,var(--screen) 70%);overflow:hidden}
.abs{position:absolute}
.brand{position:absolute;left:20px;top:18px;display:flex;align-items:center;gap:5px;font-weight:700;font-size:20px;color:var(--ink)}
.brand .dot{width:8px;height:8px;border-radius:50%;background:var(--ink)}
.nav{position:absolute;top:22px;right:18px;display:flex;gap:12px;align-items:center}
.photo{position:absolute;border-radius:50%;background:radial-gradient(circle at 45% 45%,#c9643c 0%,#7aa43e 30%,#e9d7b0 60%,#efe5d0 100%)}
.btn{position:absolute;border-radius:24px;display:flex;align-items:center;justify-content:center;font-weight:700;font-size:11px;text-transform:uppercase}
.btn.solid{background:var(--slate);color:#fff}
.btn.ghost{border:2px solid var(--slate);color:var(--slate);background:#fff}
.stars{color:var(--star);font-size:9px;letter-spacing:1px}
.macros{color:var(--gold);font-size:7px}
.back{position:absolute;font-size:13px;color:var(--ink)}
.round{border-radius:50%;display:flex;align-items:center;justify-content:center}
/* salad cards */
.card{position:absolute;left:6px;width:221px;height:85px;background:#fff;border-radius:43px;box-shadow:0 3px 10px rgba(120,100,60,.12)}
.card .photo{left:6px;top:8px;width:68px;height:68px}
.card h3{position:absolute;left:85px;top:14px;font-size:10px;font-weight:500}
.card .macros{position:absolute;left:85px;top:29px}
.card p{position:absolute;left:85px;top:44px;font-size:7.5px;color:#333}
.card .stars{position:absolute;left:85px;top:60px}
.card .fav{position:absolute;left:156px;top:61px;width:18px;height:18px;background:#ddd2ba}
.card .add{position:absolute;left:180px;top:61px;width:18px;height:18px;background:var(--gold)}
.ing{position:absolute;top:436px;width:38px;height:38px;border:2px solid #e6e6e6;background:#fff}
.qty{position:absolute;right:14px;display:flex;flex-direction:column;align-items:center;gap:6px;font-size:8px}
.qty span.c{width:14px;height:14px;border:1px solid #222;border-radius:50%;display:flex;align-items:center;justify-content:center;font-size:10px;line-height:1}
.sum-row{display:flex;justify-content:space-between;font-size:9px;margin-bottom:10px}
</style>
</head>
<body>

<!-- Screen 1: Home -->
<section class="screen" style="left:99px;top:160px;height:662px">
  <div class="brand"><span class="dot"></span>Verdi</div>
  <div class="nav">
    <svg width="12" height="14" viewBox="0 0 12 14"><circle cx="6" cy="4" r="3.5" fill="#111"/><path d="M0 14c0-4 2.5-6 6-6s6 2 6 6z" fill="#111"/></svg>
    <svg width="12" height="10" viewBox="0 0 12 10"><path d="M0 1h12M0 5h12M0 9h12" stroke="#111" stroke-width="1.4"/></svg>
  </div>
  <div class="abs" role="img" aria-label="Bowl of fresh salad with tossed vegetables flying above it" style="left:25px;top:71px;width:162px;height:187px;border-radius:50%;background:radial-gradient(circle at 50% 55%,#6fa838 0%,#9cc85a 35%,#e6ddc6 70%,rgba(242,236,221,0) 100%)"></div>
  <div class="abs" style="left:0;width:233px;top:286px;text-align:center">
    <div style="font-size:11px;font-weight:500">WELCOME TO</div>
    <div style="font-size:38px;font-weight:700;line-height:1.05">Verdi</div>
  </div>
  <p class="abs" style="left:14px;width:205px;top:352px;text-align:center;font-size:11px;line-height:18.7px;color:#4a5667">At vero eos et accusamus et iusgnissimos ducimus qui blanditiis praesentium voluptatum deleniti atque corrupti quos dolores et quas molestias excepturi sint occaecati cupiditate non provident</p>
  <a class="btn solid" style="left:35px;top:491px;width:162px;height:45px">Create your salad</a>
  <a class="btn ghost" style="left:35px;top:544px;width:162px;height:44px">Our salads</a>
</section>

<!-- Screen 2: Create your salad -->
<section class="screen" style="left:369px;top:194px;height:596px">
  <div class="brand"><span class="dot"></span>Verdi</div>
  <div class="nav">
    <svg width="12" height="14" viewBox="0 0 12 14"><circle cx="6" cy="4" r="3.5" fill="#111"/><path d="M0 14c0-4 2.5-6 6-6s6 2 6 6z" fill="#111"/></svg>
    <svg width="12" height="10" viewBox="0 0 12 10"><path d="M0 1h12M0 5h12M0 9h12" stroke="#111" stroke-width="1.4"/></svg>
  </div>
  <span class="back" style="left:18px;top:68px">&#8249;</span>
  <h2 class="abs" style="left:45px;top:66px;font-size:15.5px;font-weight:400">Create your salad</h2>
  <span class="abs round" style="left:196px;top:67px;width:18px;height:18px;background:#ddd2ba">
    <svg width="9" height="8" viewBox="0 0 10 9"><path d="M5 9L1 5a2.5 2.5 0 0 1 4-3 2.5 2.5 0 0 1 4 3z" fill="#fff"/></svg></span>
  <div class="photo" role="img" aria-label="Bowl of salad with grains, berries and dressing" style="left:54px;top:98px;width:125px;height:106px"></div>
  <svg class="abs" style="left:56px;top:212px" width="126" height="28" viewBox="0 0 126 28">
    <g fill="none" stroke="#111" stroke-width="1.4"><circle cx="14" cy="14" r="13"/><circle cx="62" cy="14" r="13"/><circle cx="108" cy="14" r="13"/><circle cx="108" cy="14" r="9"/><path d="M6 14h16M56 20l12-12"/></g>
  </svg>
  <div class="stars abs" style="left:17px;top:263px;font-size:12px">★★★★★</div>
  <div class="abs" style="left:169px;top:263px;width:37px;height:14px;border-radius:7px;background:var(--gold);color:#fff;font-size:8px;display:flex;justify-content:space-around;align-items:center"><span>-</span><span>1</span><span>+</span></div>
  <h3 class="abs" style="left:17px;top:279px;font-size:12.5px;font-weight:400">Dream On Salad</h3>
  <div class="abs" style="left:156px;top:287px;font-size:7.5px;color:#333"><span style="color:var(--red)">&#9719;</span> 10 - 15 mins</div>
  <div class="macros abs" style="left:17px;top:297px;font-size:10px">36 SR 27 SR &nbsp; 311 KCAL</div>
  <div class="abs" style="left:17px;top:310px;font-size:15px">$56.29</div>
  <p class="abs" style="left:17px;width:205px;top:334px;font-size:8.5px;line-height:13.7px;color:#333">Pperspiciatisnitusm doloremque laudantium, totam rem aperiam, eaque ipsa quae ab illo inventore veritatis et ichitecto beatae</p>
  <div class="abs" style="left:11px;width:211px;top:389px;border-top:1px solid var(--line)"></div>
  <h4 class="abs" style="left:17px;top:408px;font-size:12px;font-weight:400">Select Ingredients</h4>
  <a class="abs" style="left:183px;top:410px;font-size:10px;color:var(--red);text-decoration:underline">Clear</a>
  <span class="ing round" style="left:18px"><svg width="16" height="16" viewBox="0 0 16 16"><path d="M8 15V6M8 9C4 9 3 5 3 4c3 0 5 2 5 5zM8 11c3 0 5-3 5-5-3 0-5 2-5 5z" fill="#4e8b2e"/></svg></span>
  <span class="abs round" style="left:46px;top:430px;width:14px;height:14px;background:var(--gold)"><svg width="8" height="7" viewBox="0 0 8 7"><path d="M1 3.5l2 2 4-4.5" stroke="#fff" stroke-width="1.4" fill="none"/></svg></span>
  <span class="ing round" style="left:69px"><svg width="12" height="18" viewBox="0 0 12 18"><ellipse cx="6" cy="7" rx="5" ry="6.5" fill="#f5d64a"/><path d="M1 11h10l-2 6H3z" fill="#5ec8d8"/></svg></span>
  <span class="ing round" style="left:121px"><svg width="18" height="18" viewBox="0 0 18 18"><rect x="11" y="4" width="5" height="13" rx="1.5" fill="#7a3a18"/><circle cx="4" cy="15" r="1.6" fill="#333"/><circle cx="8" cy="15" r="1.6" fill="#333"/></svg></span>
  <span class="ing round" style="left:172px"><svg width="12" height="18" viewBox="0 0 12 18"><rect x="4" y="0" width="4" height="4" fill="#333"/><rect x="1" y="4" width="10" height="13" rx="2" fill="#e2b23c" stroke="#333"/></svg></span>
  <div class="abs" style="left:11px;width:211px;top:494px;border-top:1px solid var(--line)"></div>
  <div class="abs" style="left:15px;top:517px;font-size:8.5px">Total Price</div>
  <div class="abs" style="left:15px;top:532px;font-size:18px">$56.29</div>
  <a class="btn solid" style="left:116px;top:514px;width:101px;height:32px;font-size:8px;gap:8px">Add to cart <span class="round" style="width:15px;height:15px;background:var(--gold)"><svg width="8" height="7" viewBox="0 0 8 7"><path d="M0 1h1.5l1 4h4l1-3H2.2" stroke="#fff" fill="none"/></svg></span></a>
</section>

<!-- Screen 3: Our Salads -->
<section class="screen" style="left:625px;top:108px;height:759px">
  <div class="brand"><span class="dot"></span>Verdi</div>
  <div class="nav">
    <svg width="12" height="14" viewBox="0 0 12 14"><circle cx="6" cy="4" r="3.5" fill="#111"/><path d="M0 14c0-4 2.5-6 6-6s6 2 6 6z" fill="#111"/></svg>
    <svg width="12" height="10" viewBox="0 0 12 10"><path d="M0 1h12M0 5h12M0 9h12" stroke="#111" stroke-width="1.4"/></svg>
  </div>
  <div class="abs" style="left:16px;width:201px;top:82px;display:flex;align-items:center;gap:8px">
    <span style="flex:1;border-top:1px solid #d9d0bd"></span>
    <h2 style="font-size:20px;font-weight:500">Our Salads</h2>
    <span style="flex:1;border-top:1px solid #d9d0bd"></span>
  </div>

  <article class="card" style="top:110px"><div class="photo" role="img" aria-label="Dream On Salad bowl"></div><h3>Dream On Salad</h3><div class="macros">36 SR 27 SR &nbsp; 311 KCAL</div><p>Pperspiciatisniste natus</p><div class="stars">★★★★★</div><span class="fav round"></span><span class="add round"></span></article>
  <article class="card" style="top:204px"><div class="photo" role="img" aria-label="Kale Caesar Salad bowl"></div><h3>Kale Caesar Salad</h3><div class="macros">36 SR 27 SR &nbsp; 311 KCAL</div><p>Pperspiciatisniste natus</p><div class="stars">★★★★★</div><span class="fav round"></span><span class="add round"></span></article>
  <article class="card" style="top:299px"><div class="photo" role="img" aria-label="True Salad bowl"></div><h3>True Salad</h3><div class="macros">36 SR 27 SR &nbsp; 311 KCAL</div><p>Pperspiciatisniste natus</p><div class="stars">★★★★★</div><span class="fav round"></span><span class="add round"></span></article>
  <article class="card" style="top:393px"><div class="photo" role="img" aria-label="Halloumi Salad bowl"></div><h3>Halloumi Salad</h3><div class="macros">36 SR 27 SR &nbsp; 311 KCAL</div><p>Pperspiciatisniste natus</p><div class="stars">★★★★★</div><span class="fav round"></span><span class="add round"></span></article>
  <article class="card" style="top:488px"><div class="photo" role="img" aria-label="Korean Salad bowl"></div><h3>Korean Salad</h3><div class="macros">36 SR 27 SR &nbsp; 311 KCAL</div><p>Pperspiciatisniste natus</p><div class="stars">★★★★★</div><span class="fav round"></span><span class="add round"></span></article>
  <article class="card" style="top:582px"><div class="photo" role="img" aria-label="Crab Salad bowl"></div><h3>Crab Salad</h3><div class="macros">36 SR 27 SR &nbsp; 311 KCAL</div><p>Pperspiciatisniste natus</p><div class="stars">★★★★★</div><span class="fav round"></span><span class="add round"></span></article>

  <a class="btn solid" style="left:36px;top:686px;width:162px;height:45px">View more salads</a>
</section>

<!-- Screen 4: Cart -->
<section class="screen" style="left:881px;top:198px;height:566px">
  <div class="brand"><span class="dot"></span>Verdi</div>
  <div class="nav">
    <svg width="12" height="14" viewBox="0 0 12 14"><circle cx="6" cy="4" r="3.5" fill="#111"/><path d="M0 14c0-4 2.5-6 6-6s6 2 6 6z" fill="#111"/></svg>
    <svg width="12" height="10" viewBox="0 0 12 10"><path d="M0 1h12M0 5h12M0 9h12" stroke="#111" stroke-width="1.4"/></svg>
  </div>
  <span class="back" style="left:24px;top:76px">&#8249;</span>
  <h2 class="abs" style="left:0;width:233px;top:72px;text-align:center;font-size:20px;font-weight:500">Cart</h2>

  <article class="card" style="top:116px;width:220px">
    <div class="photo" role="img" aria-label="Dream On Salad bowl"></div>
    <h3 style="left:85px">Dream On Salad</h3><div class="macros">36 SR 27 SR &nbsp; 311 KCAL</div>
    <div class="abs" style="left:85px;top:50px;font-size:15px;color:#333">$56.29</div>
    <div class="qty" style="top:22px"><span class="c">+</span>1<span class="c">−</span></div>
  </article>
  <article class="card" style="top:211px;width:220px">
    <div class="photo" role="img" aria-label="Kale Caesar Salad bowl"></div>
    <h3 style="left:85px">Kale Caesar Salad</h3><div class="macros">36 SR 27 SR &nbsp; 311 KCAL</div>
    <div class="abs" style="left:85px;top:48px;font-size:15px;color:#333">$56.29</div>
    <div class="qty" style="top:20px"><span class="c">+</span>1<span class="c">−</span></div>
  </article>

  <div class="abs" style="left:13px;top:320px;width:208px;height:32px;background:var(--cream-deep);font-size:9px;padding:10px 11px">Have a coupon code?</div>
  <div class="abs" style="left:13px;top:361px;width:208px;height:81px;background:#fff;padding:10px 11px">
    <div class="sum-row"><span>SubTotal</span><span style="width:45px">$56.29 *2</span></div>
    <div class="sum-row"><span>Delivery Fees</span><span style="width:45px">$5:00</span></div>
    <div class="sum-row"><span>Tax</span><span style="width:45px">-</span></div>
  </div>
  <a class="btn solid" style="left:36px;top:455px;width:162px;height:45px">Checkout &nbsp;$117.00</a>
</section>

</body>
</html>
```